Bref créative
Business cards, stationary, envelopes for investment firm
Whitford Crest Holdings
Simple
Mark L. Tressel
Principal
4618 W. Pellham Avenue, Suite 207
Corbin Falls, NV 89142
mark@whitfordch.com
www.whitfordch.com
Please provide a design that is clean and simple. Also, we require files with editable text as well.
Please use design logo in your design

```html
<!DOCTYPE html>
<html lang="en">
<head>
<meta charset="utf-8">
<title>Whitford Crest Holdings — Business Card</title>
<link href="https://fonts.googleapis.com/css2?family=Cinzel:wght@400;500;600&display=swap" rel="stylesheet">
<style>
  :root {
    --page-bg: #e9e7e3;
    --card-white: #ffffff;
    --navy: #2f3c80;
    --wave-grey: #6d6e72;
    --text-white: #ffffff;
    --text-navy: #2f3c80;
    --shadow: rgba(0, 0, 0, 0.18);
  }
  * { margin: 0; padding: 0; box-sizing: border-box; }
  html, body {
    width: 1200px;
    height: 900px;
    overflow: hidden;
    background: var(--page-bg);
    font-family: "Cinzel", "Times New Roman", serif;
  }
  .stage {
    width: 1200px;
    height: 900px;
    display: flex;
    align-items: center;
    justify-content: center;
  }
  .business-card {
    position: relative;
    width: 1000px;
    height: 571px;
    background: var(--card-white);
    box-shadow: 0 14px 40px var(--shadow);
    overflow: hidden;
  }
  .card-waves {
    position: absolute;
    inset: 0;
    width: 100%;
    height: 100%;
  }
  .wave-grey { fill: var(--wave-grey); }
  .wave-navy { fill: var(--navy); }
  .brand {
    position: absolute;
    top: 92px;
    left: 262px;
    display: flex;
    align-items: center;
    gap: 20px;
  }
  .brand-dot {
    width: 64px;
    height: 64px;
    border-radius: 50%;
    background: var(--navy);
    flex: none;
  }
  .brand-name {
    color: var(--text-navy);
    font-weight: 500;
    line-height: 1;
  }
  .brand-name .line-main {
    display: block;
    font-size: 44px;
    letter-spacing: 0.5px;
  }
  .brand-name .line-sub {
    display: block;
    font-size: 19px;
    letter-spacing: 7px;
    margin-top: 8px;
  }
  .contact-list {
    position: absolute;
    left: 42px;
    top: 352px;
    list-style: none;
    color: var(--text-white);
    font-size: 15px;
    line-height: 1;
  }
  .contact-item {
    display: flex;
    align-items: center;
    gap: 9px;
    height: 24px;
    letter-spacing: 0.3px;
  }
  .contact-icon {
    width: 15px;
    height: 15px;
    flex: none;
  }
  .icon-disc { fill: var(--text-white); }
  .icon-mark { fill: var(--navy); }
  .icon-line { fill: none; stroke: var(--navy); stroke-width: 0.9; }
  .person {
    position: absolute;
    right: 52px;
    top: 360px;
    text-align: right;
    color: var(--text-white);
  }
  .person-name {
    font-size: 26px;
    font-weight: 500;
    letter-spacing: 0.5px;
  }
  .person-title {
    font-size: 15px;
    margin-top: 10px;
    letter-spacing: 0.5px;
  }
</style>
</head>
<body>
<main class="stage">
  <article class="business-card">
    <svg class="card-waves" viewBox="0 0 1000 571" preserveAspectRatio="none" aria-hidden="true">
      <path class="wave-grey"
        d="M0 268 C 230 214, 440 312, 640 270 C 800 236, 900 196, 1000 206 L1000 228 C 900 220, 800 258, 640 290 C 440 332, 230 236, 0 290 Z"/>
      <path class="wave-navy"
        d="M0 304 C 230 252, 440 348, 640 306 C 800 272, 900 236, 1000 246 L1000 571 L0 571 Z"/>
    </svg>

    <div class="brand">
      <span class="brand-dot"></span>
      <div class="brand-name">
        <span class="line-main">WHITFORD CREST</span>
        <span class="line-sub">HOLDINGS</span>
      </div>
    </div>

    <ul class="contact-list">
      <li class="contact-item">
        <svg class="contact-icon" viewBox="0 0 16 16"><circle class="icon-disc" cx="8" cy="8" r="8"/><path class="icon-mark" d="M8 3.5a2.8 2.8 0 0 0-2.8 2.8C5.2 8.5 8 12.5 8 12.5s2.8-4 2.8-6.2A2.8 2.8 0 0 0 8 3.5z"/><circle class="icon-disc" cx="8" cy="6.3" r="1"/></svg>
        <span>4618 W. Pellham Avenue, Suite 207</span>
      </li>
      <li class="contact-item">
        <svg class="contact-icon" viewBox="0 0 16 16"><circle class="icon-disc" cx="8" cy="8" r="8"/></svg>
        <span>Corbin Falls, NV 89142</span>
      </li>
      <li class="contact-item">
        <svg class="contact-icon" viewBox="0 0 16 16"><circle class="icon-disc" cx="8" cy="8" r="8"/><path class="icon-mark" d="M5 4h2l.8 2-1.2.9a6 6 0 0 0 2.5 2.5l.9-1.2 2 .8v2c0 .6-.5 1-1 1A7 7 0 0 1 4 5c0-.5.4-1 1-1z"/></svg>
        <span>480-555-0147</span>
      </li>
      <li class="contact-item">
        <svg class="contact-icon" viewBox="0 0 16 16"><circle class="icon-disc" cx="8" cy="8" r="8"/><rect class="icon-mark" x="5.5" y="3.5" width="5" height="9" rx="1"/><rect class="icon-disc" x="6.5" y="4.8" width="3" height="5.4"/></svg>
        <span>480-555-0162</span>
      </li>
      <li class="contact-item">
        <svg class="contact-icon" viewBox="0 0 16 16"><circle class="icon-disc" cx="8" cy="8" r="8"/><rect class="icon-mark" x="4" y="6.5" width="8" height="5" rx="0.8"/><rect class="icon-mark" x="5.5" y="4" width="5" height="3"/></svg>
        <span>480-555-0189</span>
      </li>
      <li class="contact-item">
        <svg class="contact-icon" viewBox="0 0 16 16"><circle class="icon-disc" cx="8" cy="8" r="8"/><rect class="icon-mark" x="4" y="5" width="8" height="6" rx="0.6"/><path d="M4.3 5.4 8 8.3l3.7-2.9" stroke="#fff" stroke-width="0.9" fill="none"/></svg>
        <span>mark@whitfordch.com</span>
      </li>
      <li class="contact-item">
        <svg class="contact-icon" viewBox="0 0 16 16"><circle class="icon-disc" cx="8" cy="8" r="8"/><circle class="icon-line" cx="8" cy="8" r="4.2"/><path class="icon-line" d="M3.8 8h8.4M8 3.8c-2 2.5-2 5.9 0 8.4M8 3.8c2 2.5 2 5.9 0 8.4"/></svg>
        <span>www.whitfordch.com</span>
      </li>
    </ul>

    <div class="person">
      <p class="person-name">Mark L. Tressel</p>
      <p class="person-title">Principal</p>
    </div>
  </article>
</main>
</body>
</html>
```